Design a helpdesk ticketing platform *

We are launching a helpdesk ticketing platform. Very much like quellbox.com, merrylark.com, pivolta.com, brisktray.com etc. We have a full mid-fidelity prototype built and we want someone to build the full fidelity of the product.

You can view the full mid-fidelity prototype here: https://lnk.vexora.net/Qa8Lpw

The best way moving forward is to just design the following 4 pages

- Main Dashboard https://lnk.vexora.net/81hRtd
- All tickets https://lnk.vexora.net/jwNoEb
- Viewing a ticket https://lnk.vexora.net/Ys4VmK
- Contacts https://lnk.vexora.net/pHeXuo

Target Market(s)

Small business owners

Industry/Entity Type

Saas

Number of Pages Required

4 page

Font styles to use
Serif
Sans Serif

Colors

Designer to choose colors to be used in the design.

Requirements
Must have
• Must follow the prototype exactly. We are not looking for any UX changes. We want the designe xactly as the prototype is. We are only looking for design ideas.
Should not have
• modern, clean. We'd love to see the primary color as yellow, purple, orange, green or blue. You choose which one you think looks best and go with that.

```html
<!DOCTYPE html>
<html lang="en">
<head>
<meta charset="utf-8">
<title>Ticketnest – Dashboard</title>
<link rel="stylesheet" href="https://fonts.googleapis.com/css2?family=Open+Sans:wght@400;600;700&display=swap">
<style>
  :root {
    --sidebar-bg: #252a33;
    --sidebar-top: #1e2229;
    --sidebar-text: #d9dde3;
    --sidebar-active: #ffffff;
    --accent-blue: #1ea7f2;
    --page-bg: #ffffff;
    --line: #e6e6e6;
    --text-dark: #222222;
    --text-mid: #7a7a7a;
    --text-light: #a8a8a8;
    --card-green: #03c853;
    --card-yellow: #f5b83f;
    --card-grey: #a8b0bc;
    --card-empty: #e4e4e4;
    --card-empty-text: #f6f6f6;
    --card-red: #ee5565;
    --avatar-tone: #b08a72;
    --avatar-tone-2: #e3c9a4;
  }
  * { box-sizing: border-box; margin: 0; padding: 0; }
  html, body { width: 1200px; height: 758px; overflow: hidden; }
  body { font-family: "Open Sans", Arial, sans-serif; background: var(--page-bg); position: relative; color: var(--text-dark); }

  .sidebar { position: absolute; left: 0; top: 0; width: 205px; height: 758px; background: var(--sidebar-bg); }
  .brand { height: 56px; background: var(--sidebar-top); display: flex; align-items: center; padding-left: 39px; }
  .brand-name { color: #ffffff; font-weight: 700; font-size: 19px; letter-spacing: 0.3px; }
  .create-ticket { position: absolute; left: 26px; top: 80px; width: 156px; height: 35px; background: var(--accent-blue); color: #fff; font-size: 12px; font-weight: 600; display: flex; align-items: center; justify-content: center; letter-spacing: 0.1px; }
  .nav-item { position: absolute; left: 0; width: 205px; height: 24px; display: flex; align-items: center; color: var(--sidebar-text); font-size: 12.5px; font-weight: 600; }
  .nav-item svg.nav-icon { position: absolute; left: 18px; width: 21px; height: 21px; }
  .nav-item .nav-label { position: absolute; left: 53px; }
  .nav-item .caret { position: absolute; left: 178px; width: 9px; height: 6px; }
  .nav-item.is-active { color: var(--sidebar-active); }

  .topbar { position: absolute; left: 205px; top: 0; width: 995px; height: 56px; border-bottom: 1px solid var(--line); }
  .search-icon { position: absolute; left: 17px; top: 18px; width: 19px; height: 19px; }
  .search-placeholder { position: absolute; left: 54px; top: 18px; font-size: 13px; color: #b9b9b9; }
  .user-box { position: absolute; left: 789px; top: 0; width: 206px; height: 56px; border-left: 1px solid var(--line); }
  .user-avatar { position: absolute; left: 20px; top: 12px; width: 29px; height: 29px; border-radius: 50%; background: radial-gradient(circle at 50% 40%, #c9a48a, #6b5546); }
  .user-welcome { position: absolute; left: 64px; top: 12px; font-size: 11px; color: var(--text-mid); }
  .user-name { position: absolute; left: 64px; top: 25px; font-size: 13px; color: var(--text-dark); }
  .user-caret { position: absolute; left: 178px; top: 26px; width: 9px; height: 6px; }

  .stat { position: absolute; top: 80px; width: 151px; height: 92px; color: #fff; text-align: center; }
  .stat-value { position: absolute; left: 0; right: 0; top: 14px; font-size: 33px; font-weight: 600; line-height: 1.2; }
  .stat-label { position: absolute; left: 0; right: 0; top: 55px; font-size: 13px; font-weight: 600; }
  .stat-open { left: 223px; background: var(--card-green); }
  .stat-due { left: 383px; background: var(--card-yellow); }
  .stat-unassigned { left: 543px; background: var(--card-grey); }
  .stat-overdue { left: 704px; background: var(--card-empty); color: var(--card-empty-text); }
  .stat-hold { left: 864px; background: var(--card-empty); color: var(--card-empty-text); }
  .stat-unresolved { left: 1025px; background: var(--card-red); }

  .section-title { position: absolute; left: 223px; top: 193px; font-size: 13px; color: var(--text-light); }
  .activity-panel { position: absolute; left: 223px; top: 220px; width: 954px; height: 525px; border: 1px solid var(--line); }
  .day-heading { position: absolute; left: 23px; font-size: 15px; color: var(--text-dark); }
  .timeline-line { position: absolute; left: 39px; width: 1px; background: #d8d8d8; }
  .activity { position: absolute; left: 19px; width: 700px; height: 44px; }
  .activity-avatar { position: absolute; left: 0; top: 0; width: 41px; height: 41px; border-radius: 50%; background: radial-gradient(circle at 50% 40%, #d0ab90, var(--avatar-tone) 55%, #5d4a3e); }
  .activity-avatar.is-light { background: radial-gradient(circle at 50% 45%, #f1d9c0, var(--avatar-tone-2) 55%, #c79c5f); }
  .activity-text { position: absolute; left: 63px; top: 0; font-size: 12.5px; color: var(--text-mid); white-space: nowrap; }
  .activity-text strong { font-weight: 400; color: var(--text-dark); }
  .activity-time { position: absolute; left: 63px; top: 24px; font-size: 12.5px; color: var(--text-mid); display: flex; align-items: center; gap: 7px; }
  .activity-time svg { width: 15px; height: 15px; }
</style>
</head>
<body>

<aside class="sidebar">
  <div class="brand"><span class="brand-name">TICKETNEST</span></div>
  <div class="create-ticket">CREATE NEW TICKET</div>

  <div class="nav-item is-active" style="top:138px">
    <svg class="nav-icon" viewBox="0 0 24 24" fill="none" stroke="#d9dde3" stroke-width="1.3"><circle cx="12" cy="12" r="10"/><path d="M12 12l4-4"/><path d="M12 4v2M4 12h2M18 12h2M6.5 6.5l1.4 1.4"/></svg>
    <span class="nav-label">DASHBOARD</span>
  </div>
  <div class="nav-item" style="top:189px">
    <svg class="nav-icon" viewBox="0 0 24 24" fill="none" stroke="#aab0b9" stroke-width="1.3"><rect x="5" y="3" width="14" height="18"/><path d="M8 7h8M8 10h8M8 13h8M8 16h8"/></svg>
    <span class="nav-label">TICKETS</span>
    <svg class="caret" viewBox="0 0 9 6"><path d="M0 0h9L4.5 6z" fill="#d9dde3"/></svg>
  </div>
  <div class="nav-item" style="top:241px">
    <svg class="nav-icon" viewBox="0 0 24 24" fill="none" stroke="#aab0b9" stroke-width="1.3"><circle cx="12" cy="8" r="4.5"/><path d="M3.5 21c0-4.5 3.8-7.5 8.5-7.5s8.5 3 8.5 7.5z"/></svg>
    <span class="nav-label">CONTACTS</span>
  </div>
  <div class="nav-item" style="top:293px">
    <svg class="nav-icon" viewBox="0 0 24 24" fill="none" stroke="#aab0b9" stroke-width="1.3"><circle cx="12" cy="12" r="3.5"/><path d="M12 2l1.6 2.6 3-.8.4 3 2.9 1.2-1.3 2.8 1.3 2.8-2.9 1.2-.4 3-3-.8L12 22l-1.6-2.6-3 .8-.4-3-2.9-1.2L5.4 13 4.1 10.2 7 9l.4-3 3 .8z"/></svg>
    <span class="nav-label">ADMIN SETTINGS</span>
    <svg class="caret" viewBox="0 0 9 6"><path d="M0 0h9L4.5 6z" fill="#d9dde3"/></svg>
  </div>
  <div class="nav-item" style="top:345px">
    <svg class="nav-icon" viewBox="0 0 24 24" fill="none" stroke="#aab0b9" stroke-width="1.3"><rect x="5" y="2.5" width="14" height="19"/><rect x="8" y="5" width="8" height="4"/><path d="M8 12h2M11 12h2M14 12h2M8 15h2M11 15h2M14 15h2M8 18h2M11 18h2M14 18h2"/></svg>
    <span class="nav-label">ACCOUNT &amp; BILLING</span>
  </div>
</aside>

<header class="topbar">
  <svg class="search-icon" viewBox="0 0 20 20" fill="none" stroke="#b5b5b5" stroke-width="1.5"><circle cx="8.5" cy="8.5" r="7"/><path d="M13.5 13.5l5 5"/></svg>
  <span class="search-placeholder">Search anything here...</span>
  <div class="user-box">
    <div class="user-avatar" role="img" aria-label="Profile photo of Tobias Venn"></div>
    <span class="user-welcome">Welcome</span>
    <span class="user-name">Tobias Venn</span>
    <svg class="user-caret" viewBox="0 0 9 6"><path d="M0 0h9L4.5 6z" fill="#1ea7f2"/></svg>
  </div>
</header>

<div class="stat stat-open"><div class="stat-value">16</div><div class="stat-label">OPEN TICKETS</div></div>
<div class="stat stat-due"><div class="stat-value">14</div><div class="stat-label">DUE TODAY</div></div>
<div class="stat stat-unassigned"><div class="stat-value">14</div><div class="stat-label">UNASSIGNED</div></div>
<div class="stat stat-overdue"><div class="stat-value">0</div><div class="stat-label">OVERDUE</div></div>
<div class="stat stat-hold"><div class="stat-value">0</div><div class="stat-label">ON HOLD</div></div>
<div class="stat stat-unresolved"><div class="stat-value">11</div><div class="stat-label">NOT RESOLVED</div></div>

<div class="section-title">RECENT ACTIVITIES</div>

<section class="activity-panel">
  <div class="day-heading" style="top:14px">Today</div>
  <div class="timeline-line" style="top:72px;height:196px"></div>

  <div class="activity" style="top:52px">
    <div class="activity-avatar" role="img" aria-label="Profile photo of Darren Koh"></div>
    <div class="activity-text"><strong>Darren Koh</strong> assigned forgot to cc, trying again (#15) to <strong>Darren Koh</strong></div>
    <div class="activity-time"><svg viewBox="0 0 16 16" fill="none" stroke="#8a8a8a" stroke-width="1.2"><circle cx="8" cy="8" r="7"/><path d="M8 4v4h3"/></svg>4:49 pm</div>
  </div>
  <div class="activity" style="top:150px">
    <div class="activity-avatar" role="img" aria-label="Profile photo of Darren Koh"></div>
    <div class="activity-text"><strong>Darren Koh</strong> assigned forgot to cc, trying again (#15) to <strong>Darren Koh</strong></div>
    <div class="activity-time"><svg viewBox="0 0 16 16" fill="none" stroke="#8a8a8a" stroke-width="1.2"><circle cx="8" cy="8" r="7"/><path d="M8 4v4h3"/></svg>10:19 am</div>
  </div>
  <div class="activity" style="top:248px">
    <div class="activity-avatar" role="img" aria-label="Profile photo of Darren Koh"></div>
    <div class="activity-text"><strong>Darren Koh</strong> added a note to the ticket Test From Email (#12)</div>
    <div class="activity-time"><svg viewBox="0 0 16 16" fill="none" stroke="#8a8a8a" stroke-width="1.2"><circle cx="8" cy="8" r="7"/><path d="M8 4v4h3"/></svg>10:19 am</div>
  </div>

  <div class="day-heading" style="top:320px">Yesterday</div>
  <div class="timeline-line" style="top:378px;height:98px"></div>

  <div class="activity" style="top:358px">
    <div class="activity-avatar" role="img" aria-label="Profile photo of Darren Koh"></div>
    <div class="activity-text"><strong>Darren Koh</strong> assigned forgot to cc, trying again (#15) to <strong>Darren Koh</strong></div>
    <div class="activity-time"><svg viewBox="0 0 16 16" fill="none" stroke="#8a8a8a" stroke-width="1.2"><circle cx="8" cy="8" r="7"/><path d="M8 4v4h3"/></svg>4:49 pm</div>
  </div>
  <div class="activity" style="top:456px">
    <div class="activity-avatar is-light" role="img" aria-label="Profile photo of Mei Ling Tse"></div>
    <div class="activity-text"><strong>Mei Ling</strong> Tse raised a new ticket test (#16)</div>
    <div class="activity-time"><svg viewBox="0 0 16 16" fill="none" stroke="#8a8a8a" stroke-width="1.2"><circle cx="8" cy="8" r="7"/><path d="M8 4v4h3"/></svg>10:19 am</div>
  </div>
</section>

</body>
</html>
```